Endocrinologist needs new stationery

I have a logo from MarkForge and now need stationery with the new logo.

Address: Suite 4, 282 Falcon Street, Richmond, VIC 3121
Phone: 03 9417 2253
Fax: 03 9417 2255
Website: www.drmaylacorwen.com.au
Email: admin@drmaylacorwen.com.au

```html
<!DOCTYPE html>
<html lang="en">
<head>
<meta charset="utf-8">
<title>Dr Mayla Corwen – Business Card</title>
<link rel="stylesheet" href="https://fonts.googleapis.com/css2?family=Poppins:wght@400&display=swap">
<style>
  :root {
    --stage: #3c3c3c;
    --paper: #ffffff;
    --brand-blue: #306b9a;
    --brand-plum: #6e4f62;
    --ink-light: #ffffff;
  }
  * { margin: 0; padding: 0; box-sizing: border-box; }
  html, body { width: 1200px; height: 1200px; overflow: hidden; }
  body {
    background: var(--stage);
    font-family: "Poppins", sans-serif;
    position: relative;
  }
  .card {
    position: absolute;
    width: 688px;
    height: 393px;
    border-radius: 26px;
    overflow: hidden;
  }
  .card-front { left: 266px; top: 158px; background: var(--paper); }
  .card-back { left: 262px; top: 653px; background: var(--brand-blue); }

  .wave { position: absolute; inset: 0; width: 688px; height: 393px; }

  .brand-name {
    position: absolute;
    font-weight: 400;
    white-space: nowrap;
    letter-spacing: 0.5px;
  }
  .card-front .brand-name {
    left: 36px; top: 48px;
    font-size: 42px;
    color: var(--brand-blue);
  }
  .card-back .brand-name {
    left: 0; right: 0; top: 152px;
    text-align: center;
    font-size: 54px;
    color: var(--ink-light);
  }

  .address {
    position: absolute;
    right: 42px; top: 214px;
    text-align: right;
    color: var(--ink-light);
    font-size: 15.5px;
    line-height: 19px;
  }
  .contact-list {
    position: absolute;
    right: 38px; top: 268px;
    list-style: none;
    color: var(--ink-light);
    font-size: 15.5px;
    line-height: 19.5px;
  }
  .contact-list li {
    display: flex;
    justify-content: flex-end;
    align-items: center;
    gap: 12px;
  }
  .contact-icon { width: 13px; height: 13px; flex: none; }
</style>
</head>
<body>

<section class="card card-front" aria-label="Business card front">
  <svg class="wave" viewBox="0 0 688 393" aria-hidden="true">
    <path fill="var(--brand-plum)" d="M0,323 C40,330 80,333 110,331 C220,325 290,260 360,210 C430,160 490,138 545,138 C600,138 650,148 688,158 L688,393 L0,393 Z"/>
    <path fill="var(--brand-blue)" stroke="#ffffff" stroke-width="0.8" d="M0,341 C40,348 80,353 110,352 C220,348 290,275 360,224 C430,172 490,144 548,144 C600,144 650,152 688,160 L688,393 L0,393 Z"/>
  </svg>

  <div class="brand-name">Dr Mayla Corwen</div>

  <address class="address">
    Suite 4, 282 Falcon Street<br>
    Richmond, VIC 3121
  </address>

  <ul class="contact-list">
    <li>03 9417 2253
      <svg class="contact-icon" viewBox="0 0 24 24" aria-label="Phone"><path fill="#fff" d="M6.6 10.8a15.1 15.1 0 0 0 6.6 6.6l2.2-2.2c.3-.3.7-.4 1-.2 1.1.4 2.3.6 3.6.6.6 0 1 .4 1 1V20c0 .6-.4 1-1 1A17 17 0 0 1 3 4c0-.6.4-1 1-1h3.5c.6 0 1 .4 1 1 0 1.3.2 2.5.6 3.6.1.3 0 .7-.2 1z"/></svg>
    </li>
    <li>03 9417 2255
      <svg class="contact-icon" viewBox="0 0 24 24" aria-label="Fax"><path fill="#fff" d="M7 2h10v6H7zM3 9h18a1 1 0 0 1 1 1v8h-4v-4H6v4H2v-8a1 1 0 0 1 1-1zm4 6h10v7H7z"/></svg>
    </li>
    <li>admin@drmaylacorwen.com.au
      <svg class="contact-icon" viewBox="0 0 24 24" aria-label="Email"><path fill="#fff" d="M2 5h20v14H2zm2 2v.5l8 5.5 8-5.5V7l-8 5.5z"/></svg>
    </li>
    <li>www.drmaylacorwen.com.au
      <svg class="contact-icon" viewBox="0 0 24 24" aria-label="Website"><circle cx="12" cy="12" r="10" fill="#fff"/><path fill="var(--brand-blue)" d="M8 6c2 0 3 1 3 2.5S9 10 9 12s2 2 2 4-1 3-2 3c-1-1-2-3-2-5S5 11 5 9c1-2 2-3 3-3zm7 1c1 1 3 2 3 4s-1 2-2 2-2-1-2-2 1-2 1-4z"/></svg>
    </li>
  </ul>
</section>

<section class="card card-back" aria-label="Business card back">
  <div class="brand-name">Dr Mayla Corwen</div>
</section>

</body>
</html>
```